Estate agent needs for sale board design to match their modern approach to selling home.

Need a for sale design for our estate agency business. We are looking for a clean look with a white background but some clever graphical elements to it. I enclose our logo so you can use this.
We need the words 'FOR SALE' and our telephone number prominent. 0808 274 5192 . The size of the boards are 640h x 813w.
Business
- Colours matching our logo.

```html
<!DOCTYPE html>
<html lang="en">
<head>
<meta charset="utf-8">
<title>For Sale Board – Keystone Homes</title>
<link rel="stylesheet" href="https://fonts.googleapis.com/css2?family=Roboto+Condensed:wght@400;500&family=Arimo:wght@700&display=swap">
<style>
  :root {
    --backdrop: #6b6b6b;
    --board: #ffffff;
    --brand-grey: #58585a;
    --brand-pink: #e8418f;
    --brand-blue: #1cb4e8;
    --brand-orange: #f39a34;
    --tint-green: #e9f2dc;
    --tint-grey: #e0e0e0;
    --tint-peach: #fde8d6;
  }
  html, body {
    margin: 0;
    width: 1200px;
    height: 1200px;
    overflow: hidden;
    background: var(--backdrop);
  }
  .board {
    position: absolute;
    left: 112px;
    top: 216px;
    width: 975px;
    height: 768px;
    background: var(--board);
    overflow: hidden;
  }
  .board__decoration {
    position: absolute;
    left: 0;
    top: 86px;
    width: 310px;
    height: 617px;
    background: linear-gradient(180deg, var(--tint-green) 0%, var(--tint-green) 35%, var(--tint-grey) 50%, var(--tint-peach) 65%, var(--tint-peach) 100%);
    opacity: 0.8;
  }
  .brand {
    position: absolute;
    left: 552px;
    top: 36px;
  }
  .brand__mark {
    position: absolute;
    left: 30px;
    top: 22px;
    width: 56px;
    height: 56px;
    background: var(--brand-pink);
  }
  .brand__name {
    position: absolute;
    left: 114px;
    top: -4px;
    margin: 0;
    font-family: "Roboto Condensed", sans-serif;
    font-weight: 400;
    font-size: 46px;
    line-height: 46px;
    color: var(--brand-grey);
    white-space: nowrap;
  }
  .brand__tagline {
    position: absolute;
    left: 114px;
    top: 83px;
    margin: 0;
    font-family: "Roboto Condensed", sans-serif;
    font-size: 20px;
    line-height: 1;
    letter-spacing: 0.5px;
    color: var(--brand-grey);
    white-space: nowrap;
  }
  .headline {
    position: absolute;
    left: 452px;
    top: 260px;
    width: 358px;
    margin: 0;
    font-family: "Roboto Condensed", sans-serif;
    font-weight: 500;
    text-align: center;
  }
  .headline__for {
    display: block;
    font-size: 78px;
    line-height: 1;
    color: var(--brand-blue);
  }
  .headline__rule {
    position: absolute;
    left: 2px;
    top: 82px;
    width: 354px;
    height: 3px;
    background: var(--brand-pink);
  }
  .headline__sale {
    position: absolute;
    left: 0;
    top: 78px;
    width: 100%;
    font-size: 180px;
    line-height: 1;
    letter-spacing: 1px;
    color: var(--brand-orange);
  }
  .contact {
    position: absolute;
    left: 380px;
    top: 595px;
    width: 500px;
    margin: 0;
    font-family: "Arimo", sans-serif;
    font-weight: 700;
    font-size: 46px;
    line-height: 1;
    text-align: center;
    color: var(--brand-pink);
    white-space: nowrap;
  }
</style>
</head>
<body>
  <main class="board">
    <div class="board__decoration" role="img" aria-label="Large faint brand decoration in soft green, grey and peach tints"></div>

    <header class="brand">
      <span class="brand__mark"></span>
      <p class="brand__name">KEYSTONE<br>HOMES</p>
      <p class="brand__tagline">selling homes the smart way</p>
    </header>

    <h1 class="headline">
      <span class="headline__for">FOR</span>
      <span class="headline__rule"></span>
      <span class="headline__sale">SALE</span>
    </h1>

    <p class="contact">Tel: 0808 274 5192</p>
  </main>
</body>
</html>
```